Timeless Estate Planning Law Firm Ad

We need an advertisement design for our Estate Planning Law Firm located in the Overland Park, Kansas. This ad will be placed in Brierfield Valley Technical Institute Stagecraft Season Guide. Inside the front cover.

I want the ad "Pop" and be very clean. Not cluttered.

The final design should target the 55+ age demographic with upper income range. We want it to have a "Call to Action" to think about their own estate planning.

Target Market(s)

Industry/Entity Type

Lawyer

Font styles to use
Serif

Requirements
Must have
• Colors:
• Red: C5/M100/B25
• Gold: C20/M50/Y100/B42
• Black: C100/M100/Y100/B100
• Requirements:
• Ad size: 4.5"w x 7.5"h
• no bleed
• MATERIALS REQUIRED FOR PRINT PRODUCTS
• * PDF/X-1a files are required for all ads.
• * Fonts must be outlined or embedded.
• * All colors should be converted to CMYK (except black text).
• * Crop marks and color bars should be outside printable area (12-point offset).
• * Only one ad per PDF document.
• DOCUMENT SETUP
• Layoutix Pro for ad layouts.
• * Photoshop: 300 dpi CMYK or grayscale, 600 dpi minimum bitmap, flattened layers, TIF or EPS format, binary encoding (no JPG and no extra channels).
• * Illustrator: Outline all fonts, flatten transparencies, embed all elements (no links).
• * All fonts should be Type 1 or OpenType (Multiple Master Fonts are strongly discouraged).
• * All colors must be CMYK (except black text); no PMS/Pantone colors.
• * Ink density is not to exceed 300%.
• * Black text 12 points or smaller should be black only.
• (C=0%, M=0%, Y=0%, K=100%).
• * Reversed text must be a minimum of 10 points.
Nice to have
• Add Thornbeck Legal Logo
• Attorney Picture: Dwight L. Thornbeck
• Ideas for titles:
• Estate Planning: If You Don't Do It, The Court Will...
• We Will Be There When You Need Us...
• Let Us Help You
• * Avoid Probate and Court Interference with Your Affairs
• * Minimize Family In-fighting
• * Protect Heirs from Wasting Inheritances
• * Keep Assets in Your Bloodline
• * Preserve and Protect IRA's and Retirement Accounts
• List Our Services:
• Family Estate Planning, Trusts, Wills, Powers of Attorney, Business Succession Planning, Probate & Trust Administration, Asset Protection Planning, Special Needs Planning
• Include our:
• Get Your Estate Plan Done Today
• Free Consultation
• (913) 546-7309
• address: 24817 Harwick Street Suite 410 Overland Park, KS 66213
• website: (913) 546-7309
• Licensed in Kansas and Missouri
• The choice of an attorney is an important decision and should not be based solely upon advertisement. (in small print along the bottom)
• Add PrimeCounsel Logo and Gavel Honors 2015 Logo
• social media
Should not have
• Cluttered

```html
<!DOCTYPE html>
<html lang="en">
<head>
<meta charset="utf-8">
<title>Thornbeck Legal – Estate Planning Ad</title>
<link href="https://fonts.googleapis.com/css2?family=Tinos:ital,wght@0,400;0,700;1,400&family=Cinzel:wght@500&family=Oswald:wght@300;500;700&family=Roboto+Condensed:wght@300;400&family=Anton&family=Yellowtail&display=swap" rel="stylesheet">
<style>
  :root{
    --red:#b3162b;
    --red-dark:#8e0f20;
    --gold:#9a7328;
    --gold-light:#e8b64a;
    --black:#151515;
    --panel:#1f1f1f;
    --grey:#7b726e;
    --grey-light:#dcdcdc;
    --white:#ffffff;
    --ink:#2a2a2a;
  }
  *{margin:0;padding:0;box-sizing:border-box}
  html,body{width:720px;height:1200px;overflow:hidden;background:var(--white)}
  .ad{position:relative;width:720px;height:1200px;overflow:hidden;background:var(--white)}

  /* Header */
  .header{position:absolute;left:0;top:0;width:666px;height:156px;
    background:linear-gradient(180deg,#c42034 0%,var(--red) 60%,var(--red-dark) 100%)}
  .header__kicker{position:absolute;left:13px;top:4px;font:700 31px/1 "Tinos",serif;color:var(--white)}
  .header__line{position:absolute;left:165px;top:48px;font:700 31px/1 "Tinos",serif;color:var(--white)}
  .header__punch{position:absolute;left:244px;top:86px;font:400 54px/1 "Anton",sans-serif;color:var(--white);letter-spacing:1px}

  /* Gavel photo band */
  .hero{position:absolute;left:0;top:156px;width:666px;height:256px;
    background:radial-gradient(ellipse at 70% 30%,#a49b95 0%,#7d746f 45%,#4c3f37 100%)}
  .brand{position:absolute;left:12px;top:172px;width:286px;height:94px;background:var(--white);
    border:5px solid var(--red);display:flex;align-items:center;justify-content:center;gap:12px;
    box-shadow:0 3px 8px rgba(0,0,0,.35)}
  .brand__mark{width:20px;height:20px;background:var(--red)}
  .brand__name{font:400 25px/1 "Tinos",serif;color:var(--ink);letter-spacing:2px;text-transform:uppercase}

  /* Message */
  .message__lead{position:absolute;left:30px;top:426px;font:700 42px/1 "Tinos",serif;color:var(--gold)}
  .message__head{position:absolute;left:34px;top:464px;font:700 53px/1 "Oswald",sans-serif;color:var(--red);letter-spacing:-.5px}
  .benefits{position:absolute;left:20px;top:534px;list-style:none}
  .benefits li{font:400 19px/26.8px "Roboto Condensed",sans-serif;color:var(--ink);padding-left:18px;position:relative}
  .benefits li::before{content:"·";position:absolute;left:0;top:0;font-weight:700}

  /* Lower swoosh + services */
  .lower{position:absolute;left:0;top:680px;width:666px;height:410px}
  .badges .badge-plain{position:absolute}
  .badge-square{left:32px;top:697px;width:118px;height:105px;background:#ececec;border:2px solid #bfbfbf;border-radius:4px;box-shadow:0 2px 4px rgba(0,0,0,.25)}
  .badge-round{left:174px;top:688px;width:124px;height:124px;border-radius:50%;background:var(--white);border:7px solid #1d2b55;box-shadow:0 0 0 2px #c9c9c9}
  .badge-wide{left:316px;top:720px;width:166px;height:58px;background:#1d2b55;border-radius:6px}

  .services{position:absolute;top:893px;list-style:none}
  .services--left{left:16px}
  .services--right{left:302px;top:889px}
  .services li{font:400 19px/29.7px "Roboto Condensed",sans-serif;color:var(--white);padding-left:22px;position:relative}
  .services li svg{position:absolute;left:0;top:7px}

  .social{position:absolute;left:254px;top:1034px;display:flex;gap:9px}
  .social span{width:20px;height:20px;border-radius:50%}

  /* Footer */
  .footer__bar{position:absolute;left:0;top:1090px;width:666px;height:32px;background:var(--black)}
  .footer__tab{position:absolute;left:172px;top:1074px;width:312px;height:48px;background:var(--black);
    clip-path:polygon(4% 0,96% 0,100% 100%,0 100%)}
  .footer__url{position:absolute;left:172px;top:1082px;width:312px;text-align:center;font:400 24px/1 "Tinos",serif;color:var(--white)}
  .footer__address{position:absolute;left:0;top:1122px;width:666px;height:40px;
    background:linear-gradient(180deg,#e4e4e4,#cfcfcf);text-align:center;font:400 22px/40px "Tinos",serif;color:var(--ink)}
  .footer__disclaimer{position:absolute;left:0;top:1172px;width:666px;text-align:center;font:italic 400 14px/1 "Tinos",serif;color:var(--ink)}

  /* Call-to-action panel */
  .fold{position:absolute;right:0;width:54px;height:40px;background:var(--red-dark)}
  .fold--top{top:307px;clip-path:polygon(0 0,100% 100%,0 100%)}
  .fold--bottom{top:956px;clip-path:polygon(0 0,100% 0,100% 100%)}
  .cta{position:absolute;left:509px;top:346px;width:211px;height:610px;border-radius:12px 0 0 12px;
    background:linear-gradient(160deg,#3a3a3a 0%,var(--panel) 40%,#0d0d0d 100%);color:var(--white);text-align:center}
  .cta__intro{position:absolute;top:18px;width:100%;font:300 22px/1 "Oswald",sans-serif;letter-spacing:.5px}
  .cta__title{position:absolute;top:58px;width:100%;font:500 28px/32px "Cinzel",serif}
  .cta__today{position:absolute;top:150px;left:32px;font:400 48px/1 "Yellowtail",cursive;color:var(--gold-light);transform:rotate(-6deg)}
  .cta__phone{position:absolute;left:498px;top:574px;width:222px;height:44px;background:var(--red);border-radius:4px 0 0 4px;
    text-align:center;font:700 32px/44px "Oswald",sans-serif;color:var(--white);letter-spacing:-.5px}
  .cta__photo{position:absolute;left:0;top:278px;width:211px;height:228px;
    background:radial-gradient(ellipse at 50% 40%,#6f6f6f 0%,#3b3b3b 55%,#1a1a1a 100%)}
  .cta__name{position:absolute;top:516px;width:100%;font:700 16px/1 "Tinos",serif;letter-spacing:.3px}
  .cta__license{position:absolute;top:542px;width:100%;font:italic 300 16px/1 "Oswald",sans-serif;color:#e6e6e6}
</style>
</head>
<body>
<div class="ad">

  <header class="header">
    <div class="header__kicker">ESTATE PLANNING:</div>
    <div class="header__line">IF YOU DON’T DO IT,</div>
    <div class="header__punch">THE COURT WILL...</div>
  </header>

  <div class="hero" role="img" aria-label="Photograph of a wooden judge's gavel resting on its sound block"></div>

  <div class="brand">
    <span class="brand__mark"></span>
    <span class="brand__name">Thornbeck Legal</span>
  </div>

  <section class="message">
    <div class="message__lead">WE WILL BE THERE</div>
    <div class="message__head">WHEN YOU NEED US</div>
    <ul class="benefits">
      <li>Avoid Probate and Court Interference with your Affairs</li>
      <li>Minimize Family Infighting</li>
      <li>Protect Heirs from Wasting Inheritances</li>
      <li>Keep Assets in Your Bloodline</li>
      <li>Preserve and Protect IRA’s and Retirement Accounts</li>
    </ul>
  </section>

  <svg class="lower" viewBox="0 0 666 410" width="666" height="410" aria-hidden="true">
    <defs>
      <linearGradient id="greyFill" x1="0" y1="0" x2="0" y2="1">
        <stop offset="0" stop-color="#6f6561"/>
        <stop offset="1" stop-color="#9a928e"/>
      </linearGradient>
      <linearGradient id="mist" x1="0" y1="0" x2="0" y2="1">
        <stop offset="0" stop-color="#ffffff"/>
        <stop offset="1" stop-color="#d9d6d4"/>
      </linearGradient>
    </defs>
    <rect x="0" y="0" width="666" height="410" fill="url(#mist)"/>
    <path d="M0 184 Q260 120 510 40 L666 0 L666 410 L0 410 Z" fill="url(#greyFill)"/>
    <path d="M0 176 Q260 112 510 32" fill="none" stroke="#8e8682" stroke-width="6" opacity=".6"/>
    <path d="M0 186 Q260 122 510 42" fill="none" stroke="var(--red)" stroke-width="5"/>
  </svg>

  <div class="badges" aria-label="Recognition badges">
    <div class="badge-plain badge-square"></div>
    <div class="badge-plain badge-round"></div>
    <div class="badge-plain badge-wide"></div>
  </div>

  <ul class="services services--left">
    <li><svg width="18" height="18" viewBox="0 0 18 18"><path d="M2 9 L7 15 L16 2" fill="none" stroke="#d42a3c" stroke-width="3" stroke-linecap="round"/></svg>Family Estate Planning</li>
    <li><svg width="18" height="18" viewBox="0 0 18 18"><path d="M2 9 L7 15 L16 2" fill="none" stroke="#d42a3c" stroke-width="3" stroke-linecap="round"/></svg>Powers of Attorney</li>
    <li><svg width="18" height="18" viewBox="0 0 18 18"><path d="M2 9 L7 15 L16 2" fill="none" stroke="#d42a3c" stroke-width="3" stroke-linecap="round"/></svg>Business Succession Planning</li>
    <li><svg width="18" height="18" viewBox="0 0 18 18"><path d="M2 9 L7 15 L16 2" fill="none" stroke="#d42a3c" stroke-width="3" stroke-linecap="round"/></svg>Probate &amp; Trust Administration</li>
  </ul>
  <ul class="services services--right">
    <li><svg width="18" height="18" viewBox="0 0 18 18"><path d="M2 9 L7 15 L16 2" fill="none" stroke="#d42a3c" stroke-width="3" stroke-linecap="round"/></svg>Trusts</li>
    <li><svg width="18" height="18" viewBox="0 0 18 18"><path d="M2 9 L7 15 L16 2" fill="none" stroke="#d42a3c" stroke-width="3" stroke-linecap="round"/></svg>Wills</li>
    <li><svg width="18" height="18" viewBox="0 0 18 18"><path d="M2 9 L7 15 L16 2" fill="none" stroke="#d42a3c" stroke-width="3" stroke-linecap="round"/></svg>Asset Protection Planning</li>
    <li><svg width="18" height="18" viewBox="0 0 18 18"><path d="M2 9 L7 15 L16 2" fill="none" stroke="#d42a3c" stroke-width="3" stroke-linecap="round"/></svg>Special Needs Planning</li>
  </ul>

  <div class="social" aria-label="Social media">
    <span style="background:#35a9e0"></span>
    <span style="background:#3b5a9a"></span>
    <span style="background:#d8503e"></span>
    <span style="background:#1f7bb6"></span>
    <span style="background:#d0342b"></span>
    <span style="background:#f08a24"></span>
  </div>

  <footer class="footer">
    <div class="footer__bar"></div>
    <div class="footer__tab"></div>
    <div class="footer__url">www.thornbecklegalkc.com</div>
    <div class="footer__address">24817 Harwick Street, Suite 410 &nbsp;| Overland Park, KS 66213</div>
    <div class="footer__disclaimer">The choice of an attorney is an important decision and should not be based solely upon advertisement.</div>
  </footer>

  <div class="fold fold--top"></div>
  <div class="fold fold--bottom"></div>
  <aside class="cta">
    <div class="cta__intro">LET US HELP YOU</div>
    <div class="cta__title">GET YOUR<br>ESTATE PLAN<br>STARTED</div>
    <div class="cta__today">Today!</div>
    <div class="cta__photo" role="img" aria-label="Portrait photograph of attorney Dwight L. Thornbeck in suit and red tie"></div>
    <div class="cta__name">DWIGHT L. THORNBECK</div>
    <div class="cta__license">Licensed in Kansas &amp; Missouri</div>
  </aside>
  <div class="cta__phone">(913) 546-7309</div>

</div>
</body>
</html>
```